Harborline Energy - needs a business card

Harborline Energy is a U.S. based diesel sourcing and distribution company that supports American oil & gas fields through providing quality product and consistent services.

Target Market(s)

Oil and Gas

Contact Information for Business Card

The background of the card must be white to ensure the logo pops.

Font styles to use
Serif
Sans Serif

Colors

Designer to choose colors to be used in the design.

Requirements
Must have
• Front of Card: Tag line: Harborline Energy, Powering America's Oil & Gas fields.
• Not sure if you guys do this part but just in case...
• Dale Menschow
• Owner/CEO
• C:555.318.4076
• E:Dmenschow@harborlineenergy.example
• W:Harborlineenergy.example
• Locations: Servicing the Powder River, DJ basin and Bakken formations.
• Back of Card: " Frac fueling is what we do. We understand how important diesel fuel is to your operation, which is why our main service line is Frac fueling. We assure our supply and stand by our service"

```html
<!DOCTYPE html>
<html lang="en">
<head>
<meta charset="utf-8">
<title>Harborline Energy – Business Card</title>
<link rel="stylesheet" href="https://fonts.googleapis.com/css2?family=Tinos:ital,wght@0,400;0,700;1,400&display=swap">
<style>
  :root {
    --backdrop: #e9e7e3;
    --card: #ffffff;
    --ink: #2a2f3a;
    --ink-soft: #3d4250;
    --brand-navy: #27345a;
    --brand-red: #b3262d;
    --card-shadow: rgba(0, 0, 0, 0.18);
  }
  * { margin: 0; padding: 0; box-sizing: border-box; }
  html, body {
    width: 1200px;
    height: 960px;
    overflow: hidden;
    background: var(--backdrop);
    font-family: "Tinos", "Times New Roman", serif;
    color: var(--ink);
  }
  .sheet {
    width: 1200px;
    height: 960px;
    display: flex;
    flex-direction: column;
    align-items: center;
    justify-content: center;
    gap: 40px;
  }
  .card {
    position: relative;
    width: 700px;
    height: 400px;
    background: var(--card);
    box-shadow: 0 10px 28px var(--card-shadow);
  }

  /* Front */
  .brand {
    position: absolute;
    top: 30px;
    left: 32px;
    display: flex;
    align-items: center;
    gap: 8px;
  }
  .brand-dot {
    width: 14px;
    height: 14px;
    border-radius: 50%;
    background: var(--brand-red);
  }
  .brand-name {
    font-size: 15px;
    font-weight: 700;
    letter-spacing: 0.04em;
    color: var(--brand-navy);
  }
  .identity {
    position: absolute;
    top: 70px;
    left: 0;
    right: 0;
    text-align: center;
  }
  .person-name {
    font-size: 34px;
    font-weight: 400;
    color: var(--ink);
  }
  .person-title {
    margin-top: 4px;
    font-size: 17px;
    color: var(--ink-soft);
  }
  .company-info {
    margin-top: 34px;
    font-size: 16px;
    line-height: 1.65;
    color: var(--ink-soft);
  }
  .company-info .company { margin-bottom: 10px; }
  .contact {
    position: absolute;
    left: 200px;
    bottom: 30px;
    font-size: 15px;
    line-height: 1.3;
    color: var(--ink-soft);
    list-style: none;
  }

  /* Back */
  .mission {
    position: absolute;
    top: 50%;
    left: 50%;
    transform: translate(-50%, -50%);
    width: 300px;
    font-size: 16px;
    line-height: 1.35;
    color: var(--ink-soft);
  }
</style>
</head>
<body>
  <main class="sheet">
    <section class="card card-front" aria-label="Business card front">
      <div class="brand">
        <span class="brand-dot"></span>
        <span class="brand-name">Harborline Energy</span>
      </div>
      <div class="identity">
        <h1 class="person-name">Dale Menschow</h1>
        <p class="person-title">Owner/CEO</p>
        <div class="company-info">
          <p class="company">Harborline Energy</p>
          <p>Powering America's Oil &amp; Gas fields</p>
          <p>Servicing the Powder River, DJ basin</p>
          <p>and Bakken formations</p>
        </div>
      </div>
      <ul class="contact">
        <li>555.318.4076</li>
        <li>Dmenschow@harborlineenergy.example</li>
        <li>Harborlineenergy.example</li>
      </ul>
    </section>

    <section class="card card-back" aria-label="Business card back">
      <p class="mission">"Frac fueling is what we do. We understand how important diesel fuel is to your operation, which is why our main service line is Frac fueling. We assure our supply and stand by our service"</p>
    </section>
  </main>
</body>
</html>
```